Halvorsen Partners Business Card

Halvorsen Partners Civil Construction
Marcus Halvorsen
CEO
555-518-6094
Marcus@HalvorsenSiteworks.example
www.HalvorsenSiteworks.example
Site Development
Utility Construction
Excavation
40876 County Lane 19
Cedar Hollow, FL 30000

Target Market(s)

Construction and government

Industry/Entity Type

Business

Contact Information for Business Card

I want an unique design that make a statement

Number of Pages Required

1 page

Font styles to use

Colors

Designer to choose colors to be used in the design.

Requirements
Must have
• unique design, feel free to modify or change the color of my logo.
Nice to have
• extra design features like spot UV, foil accents, color edges, unique paper, or any thing that would make my card pop.
• I like the feel of the image that I attached

```html
<!DOCTYPE html>
<html lang="en">
<head>
<meta charset="utf-8">
<title>Halvorsen Partners Business Card</title>
<link href="https://fonts.googleapis.com/css2?family=Cabin:wght@400;500;600;700&display=swap" rel="stylesheet">
<style>
  :root {
    --page-bg: #e9e9ea;
    --brand-blue: #2b3a7e;
    --brand-grey: #8c8c90;
    --ink: #2a2a2e;
    --ground: #26252c;
    --band: rgba(244, 245, 250, 0.9);
  }
  * { box-sizing: border-box; margin: 0; padding: 0; }
  html, body { width: 1200px; height: 1200px; overflow: hidden; }
  body {
    background: var(--page-bg);
    font-family: "Cabin", sans-serif;
    color: var(--ink);
    position: relative;
  }
  .card {
    position: absolute;
    left: 160px;
    width: 880px;
    height: 544px;
    overflow: hidden;
    box-shadow: 0 6px 18px rgba(0,0,0,0.18);
  }
  .card--front { top: 36px; }
  .card--back { top: 620px; }

  .scene {
    position: absolute; inset: 0;
    background: linear-gradient(180deg, #8f8f93 0%, #c9c9cc 30%, #bdbdc0 62%, #6f6f74 78%, #2f2e35 86%, var(--ground) 100%);
  }
  .card--back .scene {
    background:
      radial-gradient(ellipse at 50% 45%, #f4f4f5 0%, rgba(244,244,245,0) 45%),
      linear-gradient(180deg, #7d7d82 0%, #c4c4c7 35%, #d6d6d8 58%, #8a8a8e 74%, #3a3940 82%, var(--ground) 100%);
  }

  .info-band {
    position: absolute;
    left: 0; right: 0;
    top: 70px; height: 346px;
    background: var(--band);
  }

  .brand {
    position: absolute;
    display: flex; align-items: center;
  }
  .brand__mark {
    width: 16px; height: 16px;
    background: var(--brand-blue);
    flex: none;
  }
  .brand__rule {
    width: 2px; align-self: stretch;
    background: var(--brand-grey);
    margin: 0 14px;
  }
  .brand__name {
    color: var(--brand-blue);
    font-weight: 500;
    line-height: 1;
    white-space: nowrap;
  }
  .brand__tagline {
    color: var(--brand-grey);
    letter-spacing: 0.2em;
    line-height: 1;
    white-space: nowrap;
  }
  .card--front .brand { left: 66px; top: 96px; height: 84px; }
  .card--front .brand__name { font-size: 40px; }
  .card--front .brand__tagline { font-size: 24px; margin-top: 8px; }

  .person {
    position: absolute; left: 66px; top: 242px;
    font-size: 31px; font-weight: 600;
    white-space: nowrap;
  }
  .person__role {
    color: var(--brand-blue);
    text-decoration: underline;
    text-underline-offset: 5px;
    margin-right: 14px;
  }
  .person__name { color: #333338; }

  .services {
    position: absolute; left: 66px; top: 316px;
    list-style: none;
    color: var(--brand-blue);
    font-size: 29px; font-weight: 700;
    line-height: 31px;
    white-space: nowrap;
  }

  .contacts {
    position: absolute; right: 48px; top: 226px;
    list-style: none;
    text-align: right;
    font-size: 23px;
    color: #2c2c30;
    white-space: nowrap;
  }
  .contacts li {
    display: flex; align-items: center; justify-content: flex-end;
    gap: 12px;
    margin-bottom: 6px;
  }
  .contacts .lines { line-height: 26px; }
  .icon {
    width: 36px; height: 36px; flex: none;
    border-radius: 50%;
    background: var(--brand-blue);
    display: flex; align-items: center; justify-content: center;
  }
  .icon svg { width: 20px; height: 20px; }

  .card--back .brand-block {
    position: absolute; left: 0; right: 0; top: 120px;
    display: flex; flex-direction: column; align-items: center;
  }
  .card--back .brand-block .brand__mark { width: 60px; height: 60px; margin-bottom: 36px; }
  .card--back .brand__name { font-size: 41px; }
  .card--back .brand__tagline { font-size: 25px; margin-top: 6px; }
</style>
</head>
<body>

<section class="card card--front">
  <div class="scene" role="img" aria-label="Black and white photo of a cloudy sky above silhouettes of a dump truck, excavator and bulldozer on a dirt site"></div>
  <div class="info-band"></div>

  <div class="brand">
    <div class="brand__mark"></div>
    <div class="brand__rule"></div>
    <div>
      <div class="brand__name">HALVORSEN PARTNERS</div>
      <div class="brand__tagline">CIVIL CONSTRUCTION</div>
    </div>
  </div>

  <p class="person"><span class="person__role">CEO</span><span class="person__name">Marcus HALVORSEN</span></p>

  <ul class="services">
    <li>Site Development</li>
    <li>Utility Construction</li>
    <li>Excavation</li>
  </ul>

  <ul class="contacts">
    <li>
      <span class="lines">40876 County Lane 19<br>Cedar Hollow, FL 30000</span>
      <span class="icon"><svg viewBox="0 0 24 24"><path d="M12 2a7 7 0 0 0-7 7c0 5 7 13 7 13s7-8 7-13a7 7 0 0 0-7-7zm0 9.5A2.5 2.5 0 1 1 12 6.5a2.5 2.5 0 0 1 0 5z" fill="#fff"/></svg></span>
    </li>
    <li>
      <span>Marcus@HalvorsenSiteworks.example</span>
      <span class="icon"><svg viewBox="0 0 24 24"><rect x="3" y="6" width="18" height="12" rx="1" fill="none" stroke="#fff" stroke-width="2"/><path d="M3 7l9 7 9-7" fill="none" stroke="#fff" stroke-width="2"/></svg></span>
    </li>
    <li>
      <span>www.HalvorsenSiteworks.example</span>
      <span class="icon"><svg viewBox="0 0 24 24" fill="none" stroke="#fff" stroke-width="1.8"><circle cx="12" cy="12" r="9"/><ellipse cx="12" cy="12" rx="4" ry="9"/><path d="M3 12h18M5 7h14M5 17h14"/></svg></span>
    </li>
    <li>
      <span>555-518-6094</span>
      <span class="icon"><svg viewBox="0 0 24 24"><path d="M6.6 10.8a15 15 0 0 0 6.6 6.6l2.2-2.2a1 1 0 0 1 1-.25 11.4 11.4 0 0 0 3.6.57 1 1 0 0 1 1 1V20a1 1 0 0 1-1 1A17 17 0 0 1 3 4a1 1 0 0 1 1-1h3.5a1 1 0 0 1 1 1 11.4 11.4 0 0 0 .57 3.6 1 1 0 0 1-.25 1z" fill="#fff"/></svg></span>
    </li>
  </ul>
</section>

<section class="card card--back">
  <div class="scene" role="img" aria-label="Black and white photo of a bright cloudy sky with silhouettes of a bulldozer, excavator and dump truck on a construction site"></div>
  <div class="brand-block">
    <div class="brand__mark"></div>
    <div class="brand__name">HALVORSEN PARTNERS</div>
    <div class="brand__tagline">CIVIL CONSTRUCTION</div>
  </div>
</section>

</body>
</html>
```